Executive recruiting firm in need of business card design

Executive recruiting firm looking for a sleek, classy and modern business card design; card itself will be square shape, rounded edges and soft touch paper, our colors are dark blues in the navy color scale, silvers and grays. Reference our website for a better idea of our company's feel and goals at Staffbrook.com - our company message is "Employee Engagement Begins at Recruitment" this should be on the card

Industry/Entity Type

Business

```html
<!DOCTYPE html>
<html lang="en">
<head>
<meta charset="utf-8">
<title>Staffbrook – Business Card</title>
<link rel="stylesheet" href="https://fonts.googleapis.com/css2?family=Overpass:wght@300;400;600;700&display=swap">
<style>
  :root {
    --backdrop: #dfdfdd;
    --card-light: #2e2e2e;
    --card-dark: #0e0e0e;
    --disc-light: #4a4a4a;
    --disc-dark: #262626;
    --brand-ink: #c8c8c8;
    --tagline: #a5a5a5;
    --white: #ffffff;
  }
  * { box-sizing: border-box; margin: 0; padding: 0; }
  html, body {
    width: 1200px; height: 701px; overflow: hidden;
    background: var(--backdrop);
    font-family: "Overpass", sans-serif;
  }
  .canvas { position: relative; width: 1200px; height: 701px; }
  .card {
    position: absolute; top: 186px;
    width: 330px; height: 330px; border-radius: 18px;
    background: linear-gradient(135deg, var(--card-light) 0%, #1c1c1c 45%, var(--card-dark) 100%);
    overflow: hidden;
  }
  .card--front { left: 248px; }
  .card--back { left: 621px; }

  .brand-name {
    position: absolute; left: 0; right: 0; top: 128px;
    text-align: center;
    font-weight: 300; font-size: 40px; letter-spacing: 3px;
    color: var(--brand-ink); line-height: 1;
  }
  .tagline {
    position: absolute; left: 0; right: 0; top: 212px;
    text-align: center; font-size: 13px; color: var(--tagline);
  }

  .contact-disc {
    position: absolute; left: 46px; top: 46px;
    width: 238px; height: 238px; border-radius: 50%;
    background: linear-gradient(145deg, var(--disc-light) 0%, #353535 50%, var(--disc-dark) 100%);
  }
  .contact { position: absolute; left: 0; right: 0; text-align: center; color: var(--white); line-height: 1.4; }
  .contact__name { top: 88px; font-weight: 700; font-size: 19px; }
  .contact__role { top: 113px; font-size: 12.5px; }
  .contact__lines { top: 148px; font-size: 13.5px; }
  .contact__address { top: 211px; font-size: 13.5px; }
</style>
</head>
<body>
<main class="canvas">
  <section class="card card--front">
    <p class="brand-name">Staffbrook</p>
    <p class="tagline">Employee engagement begins at recruitment</p>
  </section>

  <section class="card card--back">
    <div class="contact-disc"></div>
    <p class="contact contact__name">Employee Name</p>
    <p class="contact contact__role">Managing Director</p>
    <p class="contact contact__lines">00-1234-1234-55<br>employee@staffbrook.com<br>www.staffbrook.com</p>
    <p class="contact contact__address">2480 Harbor Crest Ave, Larkmont,<br>CA 90417, USA</p>
  </section>
</main>
</body>
</html>
```